U.S. based testing, inspection, and certification (TIC) company needs a new social media design.

We need a social media design primarily for LinkedIn 1200x1200px for our U.S. based company with international capabilities for performing dozens if not hundreds of testing, inspection, and certification (TIC) services. Our primary services include calibration, chemical analysis, consulting engineering, environmental simulation, forensic engineering, materials testing, mechanical testing, and nondestructive testing. Industries we serve are aerospace/aviation, automotive, chemical, commercial properties, construction, consumer products, defense, energy storage, healthcare, insurance/legal, life science, manufacturing, oil & gas, power generation, pulp & paper, and telecommunications. https://veltrolabs.example/

Guideline hex colors (primary, secondary): #29aae2, #0b1f3b

The final design should communicate:
1. Trust, Integrity, and Independence
2. Technical Expertise and Accuracy
3. Efficiency and Speed
4. Value-Added Partnership

We previously used a hexagon design that we would like to part ways from; hexagon examples and KRV logos uploaded.

```html
<!DOCTYPE html>
<html lang="en">
<head>
<meta charset="utf-8">
<title>KRV – Precision Testing Social Posts</title>
<link rel="stylesheet" href="https://fonts.googleapis.com/css2?family=Exo+2:wght@800;900&family=Fira+Sans:wght@600;700&family=Inter:wght@400;500;600&display=swap">
<style>
  :root {
    --brand-blue: #29aae2;
    --brand-navy: #0b1f3b;
    --deep-navy: #0a1a33;
    --stage: #2f2f2f;
    --white: #ffffff;
    --ink: #0b1f3b;
    --label-ink: #111827;
  }
  * { box-sizing: border-box; margin: 0; padding: 0; }
  html, body { width: 1200px; height: 2288px; overflow: hidden; }
  body {
    background: radial-gradient(ellipse at 50% 0%, #3b3b3b 0%, var(--stage) 45%, #262626 100%);
    font-family: "Inter", Arial, sans-serif;
    position: relative;
  }
  .post {
    position: absolute; left: 112px; width: 976px; height: 975px; overflow: hidden;
    box-shadow: 0 10px 40px rgba(0,0,0,.45);
  }
  .post--blue { top: 120px; }
  .post--light { top: 1193px; }

  .post__backdrop { position: absolute; inset: 0; }
  .post--blue .post__backdrop {
    background:
      radial-gradient(ellipse at 30% 55%, rgba(120,190,235,.18) 0%, transparent 50%),
      radial-gradient(ellipse at 80% 45%, rgba(120,190,235,.14) 0%, transparent 45%),
      linear-gradient(180deg, var(--brand-blue) 0%, #1b7fc0 30%, #134f86 60%, var(--brand-navy) 100%);
  }
  .post--light .post__backdrop {
    background:
      radial-gradient(ellipse at 50% 55%, #e4e6ea 0%, transparent 60%),
      linear-gradient(180deg, #f8f8f9 0%, #eeeff1 50%, #e3e5e8 100%);
  }
  .navy-field { position: absolute; inset: 0; width: 976px; height: 975px; }

  .brand { position: absolute; left: 0; right: 0; text-align: center; font-family: "Fira Sans", Arial, sans-serif; font-weight: 700; }
  .brand__mark { display: block; font-size: 70px; line-height: 70px; letter-spacing: 8px; }
  .brand__name { display: block; font-size: 18px; line-height: 22px; }
  .post--blue .brand { top: 32px; color: var(--white); }
  .post--light .brand { top: 28px; color: var(--brand-blue); }
  .post--light .brand__mark { font-size: 60px; line-height: 60px; }
  .post--light .brand__name { font-size: 16px; }

  .kicker {
    position: absolute; left: 0; right: 0; text-align: center;
    font-family: "Fira Sans", Arial, sans-serif; font-weight: 700; font-size: 36px; line-height: 40px;
  }
  .post--blue .kicker { top: 146px; color: var(--white); }
  .post--light .kicker { top: 127px; color: var(--ink); }

  .headline {
    position: absolute; left: 0; right: 0; text-align: center;
    font-family: "Exo 2", Arial, sans-serif; font-weight: 900; font-size: 82px; line-height: 90px; letter-spacing: 1px;
  }
  .post--blue .headline { top: 184px; color: var(--white); text-shadow: 0 3px 6px rgba(0,0,0,.25); }
  .post--light .headline { top: 165px; color: var(--brand-blue); }

  .rule { position: absolute; left: 100px; width: 776px; height: 1px;
    background: linear-gradient(90deg, transparent, rgba(255,255,255,.7) 20%, rgba(255,255,255,.7) 80%, transparent); }
  .rule--upper { top: 279px; }
  .rule--lower { top: 357px; }

  .subline {
    position: absolute; top: 298px; left: 0; right: 0; text-align: center; color: var(--white);
    font-family: "Fira Sans", Arial, sans-serif; font-weight: 700; font-size: 34px; line-height: 40px;
  }

  .section-title {
    position: absolute; left: 0; right: 0; text-align: center; color: var(--white);
    font-family: "Fira Sans", Arial, sans-serif; font-weight: 600; font-size: 23px; line-height: 28px;
    text-decoration: underline; text-underline-offset: 5px; text-decoration-thickness: 2px;
  }
  .post--blue .section-title--services { top: 382px; }
  .post--blue .section-title--industries { top: 594px; }
  .post--light .section-title--industries { top: 611px; }

  .checklist { position: absolute; list-style: none; color: var(--white); font-size: 19.5px; }
  .checklist li { height: 41.5px; line-height: 41.5px; display: flex; align-items: center; white-space: nowrap; }
  .checklist .tick { width: 18px; height: 18px; margin-right: 20px; flex: none; }

  .post--blue .services { top: 430px; }
  .post--blue .industries { top: 642px; }
  .post--light .industries { top: 659px; }
  .post--blue .col-1 { left: 66px; }
  .post--blue .col-2 { left: 352px; }
  .post--blue .col-3 { left: 657px; }
  .post--light .col-1 { left: 95px; }
  .post--light .col-2 { left: 380px; }
  .post--light .col-3 { left: 686px; }

  .service-badge { position: absolute; width: 180px; text-align: center; }
  .service-badge svg { display: block; margin: 0 auto; width: 106px; height: 120px; }
  .service-badge__label { display: block; margin-top: 10px; font-size: 15px; font-weight: 500; color: var(--label-ink); line-height: 18px; }

  .web-tab { position: absolute; left: 0; top: 918px; width: 976px; height: 57px; }
  .web-tab__text {
    position: absolute; left: 0; right: 0; top: 934px; text-align: center; color: var(--white);
    font-family: "Fira Sans", Arial, sans-serif; font-weight: 700; font-size: 21px; line-height: 28px; letter-spacing: .3px;
  }
</style>
</head>
<body>

<svg width="0" height="0" style="position:absolute">
  <defs>
    <symbol id="tick" viewBox="0 0 20 20">
      <path d="M10 0.8l2.3 1.7 2.8-.2 1 2.7 2.4 1.5-.7 2.8 1.3 2.5-2 2 .1 2.8-2.8.7-1.3 2.5-2.8-.7L10 19.2l-2.3-1.7-2.8.2-1-2.7L1.5 13.5l.7-2.8L.9 8.2l2-2-.1-2.8 2.8-.7L6.9 .2l2.8.7z" fill="#ffffff"/>
      <path d="M6 10.3l2.7 2.6 5.3-5.4" fill="none" stroke="#0b1f3b" stroke-width="2.2" stroke-linecap="round" stroke-linejoin="round"/>
    </symbol>
    <linearGradient id="hexFill" x1="0" y1="0" x2="0" y2="1">
      <stop offset="0" stop-color="#29aae2"/>
      <stop offset="1" stop-color="#0b3a6e"/>
    </linearGradient>
    <symbol id="hex" viewBox="0 0 106 120">
      <polygon points="53,2 104,31 104,89 53,118 2,89 2,31" fill="url(#hexFill)" stroke="#ffffff" stroke-width="3"/>
    </symbol>
  </defs>
</svg>

<!-- Post 1: blue list layout -->
<section class="post post--blue">
  <div class="post__backdrop" role="img" aria-label="Soft blue laboratory scene with faint network lines"></div>

  <div class="brand"><span class="brand__mark">KRV</span><span class="brand__name">Veltro Technical Services</span></div>
  <h2 class="kicker">PRECISION TESTING. PROVEN INTEGRITY.</h2>
  <h1 class="headline">GLOBAL CONFIDENCE.</h1>
  <div class="rule rule--upper"></div>
  <p class="subline">INDEPENDENT TESTING. TRUSTED RESULTS.</p>
  <div class="rule rule--lower"></div>

  <h3 class="section-title section-title--services">OUR PRIMARY SERVICES INCLUDE:</h3>
  <ul class="checklist services col-1">
    <li><svg class="tick"><use href="#tick"/></svg>Calibration</li>
    <li><svg class="tick"><use href="#tick"/></svg>Chemical Analysis</li>
    <li><svg class="tick"><use href="#tick"/></svg>Consulting Engineering</li>
  </ul>
  <ul class="checklist services col-2">
    <li><svg class="tick"><use href="#tick"/></svg>Environmental Simulation</li>
    <li><svg class="tick"><use href="#tick"/></svg>Forensic Engineering</li>
    <li><svg class="tick"><use href="#tick"/></svg>Materials Testing</li>
  </ul>
  <ul class="checklist services col-3">
    <li><svg class="tick"><use href="#tick"/></svg>Mechanical Testing</li>
    <li><svg class="tick"><use href="#tick"/></svg>Non-destructive Testing</li>
  </ul>

  <h3 class="section-title section-title--industries">INDUSTRIES WE SERVE:</h3>
  <ul class="checklist industries col-1">
    <li><svg class="tick"><use href="#tick"/></svg>Aerospace/aviation</li>
    <li><svg class="tick"><use href="#tick"/></svg>Automotive</li>
    <li><svg class="tick"><use href="#tick"/></svg>Chemical</li>
    <li><svg class="tick"><use href="#tick"/></svg>Commercial Properties</li>
    <li><svg class="tick"><use href="#tick"/></svg>Construction</li>
    <li><svg class="tick"><use href="#tick"/></svg>Telecommunications</li>
  </ul>
  <ul class="checklist industries col-2">
    <li><svg class="tick"><use href="#tick"/></svg>Consumer Products</li>
    <li><svg class="tick"><use href="#tick"/></svg>Defense</li>
    <li><svg class="tick"><use href="#tick"/></svg>Energy Storage</li>
    <li><svg class="tick"><use href="#tick"/></svg>Healthcare</li>
    <li><svg class="tick"><use href="#tick"/></svg>Insurance/legal</li>
  </ul>
  <ul class="checklist industries col-3">
    <li><svg class="tick"><use href="#tick"/></svg>Life Science</li>
    <li><svg class="tick"><use href="#tick"/></svg>Manufacturing</li>
    <li><svg class="tick"><use href="#tick"/></svg>Oil &amp; Gas</li>
    <li><svg class="tick"><use href="#tick"/></svg>Power Generation</li>
    <li><svg class="tick"><use href="#tick"/></svg>Pulp &amp; Paper</li>
  </ul>

  <svg class="web-tab" viewBox="0 918 976 57">
    <rect x="0" y="965" width="976" height="5" fill="#29aae2"/>
    <rect x="0" y="970" width="976" height="5" fill="#0b1f3b"/>
    <polygon points="232,975 263,925 714,925 745,975" fill="#29aae2"/>
  </svg>
  <p class="web-tab__text">WEBSITE ADDRESS: WWW.VELTROLABS.EXAMPLE</p>
</section>

<!-- Post 2: light layout with service badges -->
<section class="post post--light">
  <div class="post__backdrop" role="img" aria-label="Faded grey laboratory scene with faint network lines"></div>
  <svg class="navy-field" viewBox="0 0 976 975" aria-hidden="true">
    <defs>
      <linearGradient id="navyFade" x1="0" y1="0" x2="0" y2="1">
        <stop offset="0" stop-color="#0b1f3b"/>
        <stop offset="1" stop-color="#081833"/>
      </linearGradient>
    </defs>
    <polygon points="0,657 485,543 976,657 976,975 0,975" fill="url(#navyFade)"/>
  </svg>

  <div class="brand"><span class="brand__mark">KRV</span><span class="brand__name">Veltro Technical Services</span></div>
  <h2 class="kicker">PRECISION TESTING. PROVEN INTEGRITY.</h2>
  <h1 class="headline">GLOBAL CONFIDENCE.</h1>

  <div class="service-badge" style="left:37px; top:273px;">
    <svg role="img" aria-label="Chemical analysis icon"><use href="#hex"/></svg>
    <span class="service-badge__label">Chemical Analysis</span>
  </div>
  <div class="service-badge" style="left:240px; top:273px;">
    <svg role="img" aria-label="Consulting engineering icon"><use href="#hex"/></svg>
    <span class="service-badge__label">Consulting Engineering</span>
  </div>
  <div class="service-badge" style="left:402px; top:349px;">
    <svg role="img" aria-label="Environmental simulation icon"><use href="#hex"/></svg>
    <span class="service-badge__label">Environmental Simulation</span>
  </div>
  <div class="service-badge" style="left:546px; top:273px;">
    <svg role="img" aria-label="Mechanical testing icon"><use href="#hex"/></svg>
    <span class="service-badge__label">Mechanical Testing</span>
  </div>
  <div class="service-badge" style="left:749px; top:273px;">
    <svg role="img" aria-label="Forensic engineering icon"><use href="#hex"/></svg>
    <span class="service-badge__label">Forensic Engineering</span>
  </div>
  <div class="service-badge" style="left:138px; top:426px;">
    <svg role="img" aria-label="Materials testing icon"><use href="#hex"/></svg>
    <span class="service-badge__label">Materials Testing</span>
  </div>
  <div class="service-badge" style="left:647px; top:426px;">
    <svg role="img" aria-label="Calibration icon"><use href="#hex"/></svg>
    <span class="service-badge__label">Calibration</span>
  </div>

  <h3 class="section-title section-title--industries">INDUSTRIES WE SERVE:</h3>
  <ul class="checklist industries col-1">
    <li><svg class="tick"><use href="#tick"/></svg>Aerospace/aviation</li>
    <li><svg class="tick"><use href="#tick"/></svg>Automotive</li>
    <li><svg class="tick"><use href="#tick"/></svg>Chemical</li>
    <li><svg class="tick"><use href="#tick"/></svg>Commercial Properties</li>
    <li><svg class="tick"><use href="#tick"/></svg>Construction</li>
    <li><svg class="tick"><use href="#tick"/></svg>Telecommunications</li>
  </ul>
  <ul class="checklist industries col-2">
    <li><svg class="tick"><use href="#tick"/></svg>Consumer Products</li>
    <li><svg class="tick"><use href="#tick"/></svg>Defense</li>
    <li><svg class="tick"><use href="#tick"/></svg>Energy Storage</li>
    <li><svg class="tick"><use href="#tick"/></svg>Healthcare</li>
    <li><svg class="tick"><use href="#tick"/></svg>Insurance/legal</li>
  </ul>
  <ul class="checklist industries col-3">
    <li><svg class="tick"><use href="#tick"/></svg>Life Science</li>
    <li><svg class="tick"><use href="#tick"/></svg>Manufacturing</li>
    <li><svg class="tick"><use href="#tick"/></svg>Oil &amp; Gas</li>
    <li><svg class="tick"><use href="#tick"/></svg>Power Generation</li>
    <li><svg class="tick"><use href="#tick"/></svg>Pulp &amp; Paper</li>
  </ul>

  <svg class="web-tab" viewBox="0 918 976 57">
    <rect x="0" y="965" width="976" height="5" fill="#29aae2"/>
    <rect x="0" y="970" width="976" height="5" fill="#0b1f3b"/>
    <polygon points="232,975 263,925 714,925 745,975" fill="#29aae2"/>
  </svg>
  <p class="web-tab__text">WEBSITE ADDRESS: WWW.VELTROLABS.EXAMPLE</p>
</section>

</body>
</html>
```